Business Card & Stationary Design Project

We are looking for some creative direction for business cards and our stationary.

We are a global logistics firm that has recently changed its name to Marrick Global Logistics and we have a new website due out tomorrow (www.marrick.com.au).

The colours of the company are rich navy tones, I would like to have business cards that fit together to make one picture on the back (possibly an old map of the world??), and the front to be modern contemporary looking.

But I am open to suggestions, so just incorporate our new logo and get going!
Updates

Hi Everyone,

Thank you for all of your designs so far and the time you have put into it.

I have asked many of you for amendments to see if we can get a final product, so with this in mind I am extending the deadline by a few days.

Good luck and thank you once again.

Please message me direct if you need any clarification.

Kind Regards
Colin

Reason: As outlined the extra 3 days is for amendments and changes to the current submissions. Thanks Colin

Industry/Entity Type

Business

```html
<!DOCTYPE html>
<html lang="en">
<head>
<meta charset="utf-8">
<title>Marrick Global Logistics – Stationery</title>
<link href="https://fonts.googleapis.com/css2?family=PT+Sans:wght@400&display=swap" rel="stylesheet">
<style>
  :root{
    --navy:#1b2f72;
    --band-top:#2456ad;
    --band-bottom:#163e86;
    --logo-wash:rgba(205,210,232,0.9);
    --ink:#1a1a1a;
    --paper:#ffffff;
    --backdrop:#e9e6e1;
    --fold:#9aa0ad;
    --map-a:#2b5fa6;
    --map-b:#1d3f7e;
  }
  *{margin:0;padding:0;box-sizing:border-box}
  html,body{width:1200px;height:900px;overflow:hidden;background:var(--backdrop)}
  body{position:relative;font-family:"PT Sans",Arial,sans-serif;color:var(--ink)}

  .sheet{position:absolute;background:var(--paper);overflow:hidden}
  .side-band{position:absolute;left:0;top:0;bottom:0;background:linear-gradient(180deg,var(--band-top),var(--band-bottom))}

  .brand{position:absolute;display:flex;align-items:center;background:var(--logo-wash)}
  .brand-name{font-family:"PT Sans",Arial,sans-serif;font-weight:400;color:var(--navy);line-height:1.1}

  .contact{list-style:none;color:var(--ink)}
  .contact li{display:flex;align-items:center;gap:5px;white-space:nowrap}
  .contact svg{flex:none;fill:var(--navy)}

  /* Letterhead */
  .letterhead{left:25px;top:28px;width:630px;height:854px}
  .letterhead .side-band{width:77px}
  .letterhead .brand{left:0;top:34px;height:90px;width:230px;padding-left:20px}
  .letterhead .brand-name{font-size:26px}
  .letterhead .contact{position:absolute;left:548px;top:54px;font-size:10px;line-height:14px}
  .letter-body{position:absolute;left:102px;top:170px;width:502px;font-size:12px;line-height:14.4px;height:630px;overflow:hidden}
  .letter-body .salutation{margin-bottom:22px}
  .letter-body p{text-align:justify}
  .letterhead .address{position:absolute;left:0;right:0;padding-left:77px;bottom:23px;text-align:center;font-size:10.5px;color:var(--navy)}

  /* Business card front */
  .card-front{left:493px;top:162px;width:312px;height:178px;box-shadow:0 0 0 1px #d8d8d8}
  .card-front .side-band{width:76px}
  .card-front .brand{left:0;top:20px;height:42px;width:140px;padding-left:26px}
  .card-front .brand-name{font-size:12px}
  .holder{position:absolute;left:88px;top:94px}
  .holder-name{font-size:14px;color:var(--navy);line-height:1.1}
  .holder-title{font-size:8.5px;color:var(--ink);margin-top:2px}
  .holder-address{font-size:7.5px;line-height:10px;margin-top:12px}
  .card-front .contact{position:absolute;left:213px;top:98px;font-size:7.5px;line-height:10.5px}

  /* Business card back */
  .card-back{left:829px;top:162px;width:340px;height:178px}
  .card-back .map-fill{position:absolute;inset:0;background:radial-gradient(ellipse at 60% 40%,var(--map-a),var(--map-b))}
  .card-back .site{position:absolute;left:22px;bottom:18px;font-size:15px;letter-spacing:.06em;color:#fff}

  /* Envelope */
  .envelope{left:447px;top:400px;width:716px;height:418px;box-shadow:0 0 0 1px #d8d8d8}
  .envelope .side-band{width:112px}
  .envelope .fold{position:absolute;left:112px;right:0;top:107px;border-top:1.5px dashed var(--fold)}
  .envelope .brand{left:0;top:136px;height:66px;width:168px;padding-left:18px}
  .envelope .brand-name{font-size:18px}
  .envelope .address{position:absolute;left:244px;bottom:15px;font-size:10.5px;color:var(--navy)}
</style>
</head>
<body>

<svg width="0" height="0" style="position:absolute" aria-hidden="true">
  <defs>
    <symbol id="icon-phone" viewBox="0 0 10 10"><path d="M2.2 0.6l1.6 1.8-0.9 1.1c0.6 1.3 1.5 2.2 2.8 2.8l1.1-0.9 1.8 1.6-1 1.6C4.6 8.5 1.5 5.4 0.6 1.6z"/></symbol>
    <symbol id="icon-mobile" viewBox="0 0 10 10"><path d="M3 0.5h4v9H3zM3.8 1.5v6h2.4v-6z"/></symbol>
    <symbol id="icon-fax" viewBox="0 0 10 10"><path d="M1 3h8v5H1zM3 0.5h4v2.5H3zM3 5.5h4v1H3z"/></symbol>
    <symbol id="icon-mail" viewBox="0 0 10 10"><path d="M0.5 2h9v6h-9zM1.4 2.8L5 5.4l3.6-2.6"/></symbol>
    <symbol id="icon-web" viewBox="0 0 10 10"><path d="M5 0.5a4.5 4.5 0 1 0 0.01 0zM5 1.6a3.4 3.4 0 1 1-0.01 0zM1.6 4.5h6.8v1H1.6zM4.5 1.6h1v6.8h-1z"/></symbol>
  </defs>
</svg>

<section class="sheet letterhead" aria-label="Letterhead">
  <div class="side-band"></div>
  <div class="brand"><p class="brand-name">Marrick<br>Global Logistics</p></div>
  <ul class="contact">
    <li><svg width="9" height="9"><use href="#icon-phone"/></svg>02 8146 3920</li>
    <li><svg width="9" height="9"><use href="#icon-mobile"/></svg>0411827365</li>
    <li><svg width="9" height="9"><use href="#icon-fax"/></svg>029417 6283</li>
    <li><svg width="9" height="9"><use href="#icon-web"/></svg>marrick.com.au</li>
  </ul>
  <div class="letter-body">
    <p class="salutation">To Whom It May Concern:</p>
    <p>Lorem ipsum dolor sit amet, consectetur adipiscing elit. Quisque sem mauris, dictum id, volutpat sed magna. In et lorem vel dolor rhoncus accumsan. Proin placerat luctus fringilla mi commodo. Vivamus et nibh viverra diam pretium sit amet mi diam, sed elementum arcu. Etiam nisl erat, egestas vitae posuere lorem. Morbi vitae quam justo, ut convallis orci. Donec pulvinar semper ligula tempus quis. Mauris id augue est. Morbi ante velit, bibendum non tate et nisl. Nullam dapibus enim nec lacus ultrices sit amet condimentum. Fusce tempor, nisl facilisis lobortis semper, purus urna placerat sapien, sed ornare odio felis ut lectus. Morbi feugiat consectetur nunc eu elementum. Suspendisse dolor dolor, laoreet vitae ornare vel, consequat sit amet leo. Maecenas ut nisi ut tortor consequat commodo vitae sed erat. Quisque lectus nisl, vestibulum placerat egestas in, viverra ut nisl.</p>
    <p>Integer vitae urna libero. Mauris elementum hendrerit est in varius. Curabitur vehicula tincidunt congue. Duis vitae dui in turpis imperdiet pellentesque. Mauris sodales nisl eget tempus semper. Praesent at ligula magna. Aenean in ante sapien.</p>
    <p>Vestibulum ullamcorper pharetra tincidunt. Duis ullamcorper tempus lorem porttitor et. Vivamus luctus erat quis est pharetra ac imperdiet. Pellentesque habitant morbi tristique senectus et netus et malesuada fames ac turpis egestas. Nam nisl risus, congue lobortis faucibus a, mattis a nibh. Sed ac pellentesque hendrerit magna at mi ullamcorper consectetur. Suspendisse convallis. Nunc et neque odio. Phasellus nec nibh ac ipsum varius condimentum lorem, in semper dolor hendrerit vel. Fusce sit amet elit ut nibh. Aenean est arcu, dignissim non porttitor nec, vulputate id lorem. Pellentesque faucibus sagittis libero, et tempor urna semper at. Phasellus mollis posuere nibh in lacinia. Class aptent taciti sociosqu ad litora torquent per conubia nostra, per inceptos himenaeos. In vitae tellus orci, at ullamcorper quam sed risus viverra imperdiet vel eu neque. Integer sollicitudin. Fusce cursus metus augue. Vivamus ligula lacus, iaculis id blandit vel, consectetur commodo, orci id interdum interdum, nunc magna pharetra nisi, vitae sapien. Quisque vel risus sapien, fermentum bibendum nisi non vestibulum pretium, dolor dolor placerat diam, a luctus ipsum ipsum in velit volutpat facilisis eu vitae tellus. Morbi fringilla feugiat vitae. Donec non mattis ligula. Quisque eu lorem dolor, faucibus sit amet elementum nulla ultricies. Sed sodales mauris. Vestibulum blandit, libero et scelerisque varius, orci magna metus sit amet magna. Etiam ac augue et sapien euismod odio nec aliquam luctus, purus ipsum viverra metus, a suscipit diet mollis massa vel fermentum.</p>
  </div>
  <p class="address">58 Harbour Lane Pyrmont NSW 2009</p>
</section>

<section class="sheet card-front" aria-label="Business card front">
  <div class="side-band"></div>
  <div class="brand"><p class="brand-name">Marrick<br>Global Logistics</p></div>
  <div class="holder">
    <p class="holder-name">Your Name Here</p>
    <p class="holder-title">Your Title Here</p>
    <p class="holder-address">58 Harbour Lane<br>Pyrmont NSW 2009</p>
  </div>
  <ul class="contact">
    <li><svg width="7" height="7"><use href="#icon-phone"/></svg>02 8146 3920</li>
    <li><svg width="7" height="7"><use href="#icon-mobile"/></svg>0411827365</li>
    <li><svg width="7" height="7"><use href="#icon-fax"/></svg>029417 6283</li>
    <li><svg width="7" height="7"><use href="#icon-mail"/></svg>colin@marrick.com.au</li>
    <li><svg width="7" height="7"><use href="#icon-web"/></svg>marrick.com.au</li>
  </ul>
</section>

<section class="sheet card-back" aria-label="Business card back">
  <div class="map-fill" role="img" aria-label="Vintage coloured map of the world on a blue ground"></div>
  <p class="site">MARRICK.COM.AU</p>
</section>

<section class="sheet envelope" aria-label="Envelope">
  <div class="side-band"></div>
  <div class="fold"></div>
  <div class="brand"><p class="brand-name">Marrick<br>Global Logistics</p></div>
  <p class="address">58 Harbour Lane Pyrmont NSW 2009</p>
</section>

</body>
</html>
```